My Book needs a front and back cover design

I need you to design my front and back cover of my book. The title of my book is : Lanterns Past Harbour
Tide Notes
7 paths to gardening calmly always

The picture that I uploaded needs to be on the front cover. On the back cover it should be excerpt from Chapter One like this :

As years have gone by I have become much more conscious about my problem with stuttering, more able to relax my muscles to alleviate it. At the age of 20, I realized that stuttering is like a demon in my head that needs to be killed and that nothing is wrong with me. Furthermore, no one can help me but myself. I'm holding the key of my future. Everything is just in my head.

With this book, I want to help you realize that nobody can help you fix your stuttering better than yourself. There's no quick-get-rid-of-stuttering cure. The cure lies inside of you.

- Lorcan Vittel, excerpt from Chapter One
----------------------------------------------------------------------------------

My name also needs to be located on the front cover.

Target Market(s)

80 million people who stutter each day

Industry/Entity Type

Psychology

Font styles to use
Serif
Sans Serif

Colors
1b1b1b
000000
333333

Requirements
Must have
• Front Cover : Full Title and subtitle and my name and my picture
• Back Cover : Excerpt from my Chapter One with my name below just as I have described in my project description
Nice to have
• Maybe black background would be the best for the front cover.

```html
<!DOCTYPE html>
<html lang="en">
<head>
<meta charset="utf-8">
<title>Tide Notes — Book Cover</title>
<link href="https://fonts.googleapis.com/css2?family=Montserrat:wght@500;700;800;900&display=swap" rel="stylesheet">
<style>
  :root {
    --page: #ffffff;
    --cover: #0a0a0a;
    --ink: #ffffff;
    --accent: #3d8fe0;
    --shade-1: #1b1b1b;
    --shade-2: #333333;
    --portrait-light: #8a6a58;
    --portrait-mid: #4a3a32;
  }
  * { margin: 0; padding: 0; box-sizing: border-box; }
  html, body { width: 709px; height: 1200px; overflow: hidden; background: var(--page); }
  body { position: relative; font-family: "Montserrat", Arial, sans-serif; color: var(--ink); }

  .spread {
    position: absolute; left: 11px; top: 11px; width: 682px; height: 478px;
    background: var(--cover); display: flex;
  }
  .back { position: relative; width: 314px; height: 100%; }
  .spine { position: relative; width: 53px; height: 100%; border-left: 1px solid var(--shade-1); border-right: 1px solid var(--shade-1); }
  .front { position: relative; flex: 1; height: 100%; overflow: hidden; }

  .portrait {
    position: absolute;
    background: radial-gradient(ellipse 38% 30% at 50% 38%, var(--portrait-light) 0%, var(--portrait-mid) 55%, transparent 100%),
                linear-gradient(180deg, transparent 0%, var(--shade-1) 70%, var(--cover) 100%);
  }

  .back-portrait { left: 16px; top: 16px; width: 64px; height: 100px; }
  .back-title { position: absolute; left: 90px; right: 10px; top: 22px; text-align: center; text-transform: uppercase; }
  .back-title .title { font-weight: 900; font-size: 22px; line-height: 1.05; }
  .back-title .subtitle { font-weight: 700; font-size: 10.5px; text-transform: none; margin-top: 6px; }
  .back-title .tagline { font-weight: 900; font-size: 22px; margin-top: 6px; letter-spacing: 0.5px; }

  .excerpt { position: absolute; left: 16px; right: 14px; top: 160px; text-align: center; font-size: 9.4px; line-height: 1.38; font-weight: 500; }
  .excerpt p { margin-bottom: 10px; }
  .excerpt .emphasis { font-weight: 800; text-transform: uppercase; }
  .excerpt .signoff { font-weight: 500; }

  .spine-text {
    position: absolute; left: 50%; top: 0; height: 100%;
    writing-mode: vertical-rl; transform: translateX(-50%);
    display: flex; justify-content: space-between; padding: 18px 0 22px;
    font-size: 11px; white-space: nowrap;
  }
  .spine-text .spine-title { font-weight: 800; }
  .spine-text .spine-title span { font-weight: 500; margin-left: 6px; }
  .spine-text .spine-author { font-weight: 700; }

  .cover-title { position: absolute; left: 0; right: 0; text-align: center; text-transform: uppercase; z-index: 2; }
  .cover-title .lead { font-weight: 900; color: var(--ink); }
  .cover-title .main { font-weight: 900; color: var(--accent); letter-spacing: 1px; }
  .cover-title .subtitle { font-weight: 700; text-transform: none; color: var(--ink); }

  .front .cover-title { top: 22px; }
  .front .lead { font-size: 30px; line-height: 1; }
  .front .main { font-size: 60px; line-height: 1; }
  .front .subtitle { font-size: 13px; margin-top: 6px; }
  .front-portrait { left: 0; right: 0; top: 150px; bottom: 0; }

  .cover {
    position: absolute; left: 150px; top: 540px; width: 410px; height: 620px;
    background: var(--cover); overflow: hidden;
  }
  .cover .cover-title { top: 30px; }
  .cover .lead { font-size: 40px; line-height: 1; }
  .cover .main { font-size: 84px; line-height: 1; }
  .cover .subtitle { font-size: 17px; margin-top: 8px; }
  .cover-portrait { left: 0; right: 0; top: 200px; bottom: 0; }
  .cover-author { position: absolute; left: 0; right: 0; bottom: 34px; text-align: center; font-weight: 800; font-size: 28px; z-index: 2; }
</style>
</head>
<body>
  <section class="spread">
    <div class="back">
      <div class="portrait back-portrait" role="img" aria-label="Small author portrait"></div>
      <div class="back-title">
        <div class="title">Tide Notes</div>
        <div class="subtitle">7 paths to gardening calmly</div>
        <div class="tagline">always</div>
      </div>
      <div class="excerpt">
        <p>As years have gone by I have become much more conscious about my problem with stuttering, more able to relax my muscles to alleviate it. At the age of 20, I realized that stuttering is like a demon in my head that needs to be killed and that nothing is wrong with me. Furthermore, no one can help me but myself. I'm holding the key of my future.</p>
        <p class="emphasis">Everything is just in my head.</p>
        <p>With this book, I want to help you realize that nobody can help you fix your stuttering better than yourself. There's no quick-get-rid-of-stuttering cure.</p>
        <p class="emphasis">The cure lies inside of you.</p>
        <p class="signoff">- Lorcan Vittel, excerpt from Chapter One</p>
      </div>
    </div>
    <div class="spine">
      <div class="spine-text">
        <div class="spine-title">TIDE NOTES<span>7 paths to gardening calmly always</span></div>
        <div class="spine-author">Lorcan Vittel</div>
      </div>
    </div>
    <div class="front">
      <div class="cover-title">
        <div class="lead">Tide</div>
        <div class="main">Notes</div>
        <div class="subtitle">7 paths to gardening calmly always</div>
      </div>
      <div class="portrait front-portrait" role="img" aria-label="Author portrait in a dark polo shirt"></div>
    </div>
  </section>

  <section class="cover">
    <div class="cover-title">
      <div class="lead">Tide</div>
      <div class="main">Notes</div>
      <div class="subtitle">7 paths to gardening calmly always</div>
    </div>
    <div class="portrait cover-portrait" role="img" aria-label="Author portrait in a dark polo shirt"></div>
    <div class="cover-author">Lorcan Vittel</div>
  </section>
</body>
</html>
```